Modernize and improve usability of our webpage www.lernwandel.ch (4 languages, mostly static content)

Need to modernize and freshen up the webpages of our association: www.lernwandel.ch We offer apprenticeship exchanges within Switzerland and abroad. Young people can inform and enroll online. We do the matchmaking with work locations and organize logistics, stay overs etc.
The webpage needs to be in 4 languages (German, French, Italian and English). The main pages will be:
- Landing page: what we do, targeted to our apprentices / young people who enroll for the stages.
- Sup-Page: Registration form for interested apprentices to sign up for the program
- Sub-Page "Company", the firms who would like to send their apprentices on a internship and info on how to join the program
- Sub-Page "Host Family", private people who would be interested in hosting the apprentices (for free) during the stages. Find out about the reqiurements for the host families
- Sub-Page "About Us", who we are, executive team, board of director, our sponsor "Corvina Circle Switzerland"
- Footer: contact (E-Mail, Telephone, WhatsApp), Bank details (IBAN Number), Partnerlogo of Corvina-Circle (see uploaded jpg), Social-Media Links (Facebook, LinkedIn)

Target Market(s)

Young people looking for a "apprenticeship" stage within Switzerland or going from Switzerland abroad

Industry/Entity Type

Apprenticeships: cooks, builders, craftsman, office support, etc.

Font styles to use
Other font styles liked:
• Lato (sans serif)

Requirements
Must have
• use colors shown on uploaded PDF-Slides: Make the BLUE the MAIN color, the ORANGE as a secondary color
Nice to have
• Forms using e.g. google forms or survey-monkey forms (external links, no code). Matching & appealing visuals showing young apprentices (can use stock photos)

```html
<!DOCTYPE html>
<html lang="en">
<head>
<meta charset="utf-8">
<title>lernwandel – Apprenticeship Exchange</title>
<link rel="stylesheet" href="https://fonts.googleapis.com/css2?family=Catamaran:wght@500;600;700&family=Open+Sans:wght@400;600;700&display=swap">
<style>
:root{
  --blue:#1e4a80;
  --navy:#14264a;
  --orange:#f25c05;
  --ink:#333d4d;
  --muted:#7b8390;
  --grey-bg:#f2f2f2;
  --footer:#0f1c2e;
  --bar:#e2e8f0;
  --white:#fff;
}
*{margin:0;padding:0;box-sizing:border-box}
html,body{width:1200px;height:4967px;overflow:hidden}
body{position:relative;font-family:"Open Sans",sans-serif;color:var(--ink);background:var(--white)}
.abs{position:absolute}
h1,h2,h3,h4{font-family:"Catamaran",sans-serif}
.label{font-size:10px;font-weight:600;color:var(--orange);text-transform:uppercase;display:flex;align-items:center;gap:10px}
.label .line{width:48px;height:2px;background:var(--orange)}
.title{color:var(--blue);font-weight:700;font-size:46px;line-height:64px}
.btn{display:flex;align-items:center;justify-content:center;background:var(--orange);color:#fff;font-size:12px;font-weight:700;border-radius:4px}
.lorem{font-size:12.5px;line-height:24px;color:var(--muted)}
.photo{position:absolute}

/* top bar */
.topbar{left:0;top:0;width:1200px;height:106px;background:var(--white)}
.logo{font-family:"Catamaran",sans-serif;font-weight:700;color:var(--orange)}
.info{display:flex;align-items:center;gap:14px;font-size:10.5px;line-height:17px;color:var(--ink)}
.info b{font-weight:600;text-transform:uppercase;font-size:10px}
.quote{left:945px;top:19px;width:168px;height:49px;background:var(--navy);color:#fff;font-size:11px;font-weight:700;border-radius:3px;display:flex;align-items:center;justify-content:center}
.nav{left:85px;top:77px;width:1028px;height:64px;background:#fff;z-index:3;display:flex;align-items:center;box-shadow:0 6px 14px rgba(0,0,0,.08)}
.nav a{position:absolute;font-size:13.5px;color:var(--ink);text-decoration:none}
.social{position:absolute;width:35px;height:35px;border-radius:3px}

/* hero */
.hero{left:0;top:106px;width:1200px;height:687px;background:linear-gradient(120deg,#3c4651 0%,#5b6570 40%,#2e3640 100%)}
.hero-badge{left:511px;top:332px;width:162px;height:33px;background:var(--blue);color:#fff;font-size:12px;display:flex;align-items:center;justify-content:center;border-radius:3px}
.hero-title{left:0;top:380px;width:1200px;text-align:center;color:#fff;font-size:62px;line-height:73px;font-weight:700}
.hero-btn{left:507px;top:548px;width:168px;height:48px;border:1.5px solid #fff;color:#fff;font-size:11px;font-weight:700;display:flex;align-items:center;justify-content:center;border-radius:3px}
.arrow{width:62px;height:60px;background:#fff;display:flex;align-items:center;justify-content:center;border-radius:3px}

/* about */
.about-badge{left:430px;top:1248px;width:104px;height:104px;border-radius:50%;background:#fff;box-shadow:0 4px 14px rgba(0,0,0,.15)}

/* services */
.services{left:0;top:1460px;width:1200px;height:820px;background:var(--grey-bg)}
.card{top:1682px;width:322px;height:313px;border-radius:6px;overflow:hidden}
.card .icon{position:absolute;left:42px;top:45px;width:66px;height:66px;background:#fff;border-radius:6px;display:flex;align-items:center;justify-content:center}
.card h3{position:absolute;left:33px;top:146px;color:#fff;font-size:24px;font-weight:600}
.card p{position:absolute;left:33px;top:210px;color:#fff;font-size:13px}
.card .more{position:absolute;left:33px;top:250px;color:#fff;font-size:14px;font-weight:700}
.card .bar{position:absolute;left:33px;top:278px;width:260px;height:3px;background:var(--orange)}
.sq{width:44px;height:63px;background:#fff;display:flex;align-items:center;justify-content:center;box-shadow:0 2px 8px rgba(0,0,0,.1)}

/* cta */
.cta{left:94px;top:2178px;width:1017px;height:208px;background:linear-gradient(90deg,#1e2c52 0%,#2b3c68 60%,#1d2b50 100%);border-radius:6px}
.cta-title{left:150px;top:2272px;color:#fff;font-size:24px;font-weight:700;font-family:"Catamaran",sans-serif}
.cta-quote{left:683px;top:2263px;width:166px;height:52px;border:1.5px solid #fff;color:#fff;font-size:14px;display:flex;align-items:center;justify-content:center;border-radius:3px}
.cta-phone{left:855px;top:2263px;width:204px;height:52px;background:#fff;color:var(--ink);font-size:15px;display:flex;align-items:center;justify-content:center;gap:12px;border-radius:3px}

/* why */
.why-item h4{color:var(--blue);font-size:21px;font-weight:600;line-height:26px}
.why-item p{font-size:12.5px;line-height:19px;color:var(--muted)}
.why-icon{width:80px;height:80px;border-radius:50%;background:#fff;box-shadow:0 4px 16px rgba(0,0,0,.1);display:flex;align-items:center;justify-content:center}

/* testimonials */
.testi-bg{left:0;top:3058px;width:1200px;height:534px;background:#f1f1f1}
.tcard{top:3257px;height:208px;background:#fff;border-radius:6px;box-shadow:0 4px 14px rgba(0,0,0,.06);padding:26px 24px}
.tcard p{font-size:12.5px;line-height:23px;color:var(--muted)}
.tcard .who{position:absolute;left:22px;top:152px;display:flex;align-items:center;gap:14px;font-size:12px;font-weight:700;color:var(--ink)}
.avatar{width:48px;height:48px;border-radius:50%;background:linear-gradient(135deg,#9aa7b3,#5a6675)}
.qmark{position:absolute;right:26px;top:152px;font-family:"Catamaran",sans-serif;font-size:46px;font-weight:700;color:var(--ink);line-height:40px}
.dot{top:3508px;width:10px;height:10px;border-radius:50%;background:#c6ccd3}

/* contact */
.form-panel{left:511px;top:3845px;width:598px;height:415px;background:#fff;box-shadow:0 6px 20px rgba(0,0,0,.07)}
.field{border:1px solid #d9dde2;border-radius:4px;font-size:12px;color:var(--muted);display:flex;align-items:center;padding-left:16px}

/* footer */
.footer{left:0;top:4406px;width:1200px;height:505px;background:var(--footer)}
.infobox{left:85px;top:4406px;width:1030px;height:151px;background:#fff;display:flex}
.infobox div{flex:1;display:flex;flex-direction:column;align-items:center;justify-content:center;gap:16px;font-size:15px;font-weight:600;color:var(--ink)}
.infobox div+div{border-left:1px solid #e4e7eb}
.ft-h{font-size:17px;font-weight:700;color:#fff;font-family:"Open Sans",sans-serif}
.ft-t{font-size:12.5px;line-height:21px;color:#c6ced9}
.ft-link{font-size:12.5px;color:#c6ced9}
.bottom{left:0;top:4911px;width:1200px;height:56px;background:var(--bar)}
</style>
</head>
<body>

<!-- top bar -->
<header class="abs topbar">
  <div class="abs logo" style="left:100px;top:14px;font-size:32px">lernwandel</div>
  <div class="abs info" style="left:430px;top:22px">
    <svg width="30" height="30" viewBox="0 0 24 24" fill="none" stroke="#1e2c52" stroke-width="1.6"><path d="M12 22s7-7 7-12a7 7 0 0 0-14 0c0 5 7 12 7 12z"/><circle cx="12" cy="10" r="2.5"/></svg>
    <div><b>Location</b><br>12 Lernweg, Bern</div>
  </div>
  <div class="abs" style="left:652px;top:20px;width:1px;height:46px;background:#1e2c52"></div>
  <div class="abs info" style="left:679px;top:22px">
    <svg width="34" height="34" viewBox="0 0 24 24" fill="none" stroke="#1e2c52" stroke-width="1.6"><circle cx="12" cy="12" r="9"/><path d="M8 12h8M13 9l3 3-3 3"/></svg>
    <div><b>Office Hours</b><br>9.00 to 7.00 [Sun: Closed]</div>
  </div>
  <div class="abs quote">REQUEST A QUOTE</div>
</header>

<nav class="abs nav">
  <a style="left:36px">Home</a>
  <a style="left:148px">About Us</a>
  <a style="left:259px">Services</a>
  <a style="left:396px">Solutions</a>
  <a style="left:508px">Team</a>
  <a style="left:609px">Gallery</a>
  <a style="left:709px">Contact Us</a>
  <span class="social" style="left:863px;background:#3b5998"></span>
  <span class="social" style="left:909px;background:#e0202a"></span>
  <span class="social" style="left:955px;background:#3aa4e8"></span>
</nav>

<!-- hero -->
<section class="abs hero" role="img" aria-label="Office team working together at a desk"></section>
<div class="abs hero-badge">WELCOME</div>
<h1 class="abs hero-title">GLOBAL EXPERTISE IN<br>APPRENTICESHIP</h1>
<div class="abs hero-btn">ABOUT COMPANY</div>
<div class="abs arrow" style="left:42px;top:490px"><svg width="22" height="16" viewBox="0 0 22 16" fill="none" stroke="#1e2c52" stroke-width="2"><path d="M21 8H2M8 2 2 8l6 6"/></svg></div>
<div class="abs arrow" style="left:1094px;top:490px"><svg width="22" height="16" viewBox="0 0 22 16" fill="none" stroke="#1e2c52" stroke-width="2"><path d="M1 8h19M14 2l6 6-6 6"/></svg></div>

<!-- about -->
<div class="abs" style="left:96px;top:916px;width:444px;height:444px;border-radius:50%;background:var(--blue)"></div>
<div class="photo" role="img" aria-label="Young apprentice answering a phone at an office desk" style="left:115px;top:922px;width:426px;height:432px;border-radius:50%;background:linear-gradient(140deg,#6d7680,#b9bfc4 55%,#3e4650)"></div>
<div class="abs about-badge"></div>
<div class="abs label" style="left:612px;top:940px">About Us <span class="line"></span></div>
<h2 class="abs title" style="left:608px;top:966px">Bridging Skills,<br>Connecting Futures</h2>
<p class="abs lorem" style="left:612px;top:1106px;width:444px">Lorem ipsum dolor sit amet, consectetur adipiscing elit, sed do eiusmod tempor incididunt ut labore et dolore magna aliqua. Ut enim ad min im veniam, quis nostrud exercitation ullamco laboris nisi ut aliquip ex ea commodo consequat. Duis aute irure dolor in reprehenderit in voluptate velit esse cillum dolore eu fugiat nulla pariatur. Excepteur sint occaecat cupidatat non proident, sunt in culpa qui officia deserunt mollit anim id est laborum.</p>
<div class="abs btn" style="left:612px;top:1294px;width:167px;height:47px">Contact Us</div>

<!-- services -->
<section class="abs services"></section>
<div class="abs label" style="left:90px;top:1543px">About Us <span class="line"></span></div>
<h2 class="abs title" style="left:88px;top:1572px">Services We Provide</h2>
<div class="abs sq" style="left:999px;top:1559px"><svg width="10" height="16" viewBox="0 0 10 16" fill="none" stroke="#111" stroke-width="2.6"><path d="M8 2 2 8l6 6"/></svg></div>
<div class="abs sq" style="left:1052px;top:1559px"><svg width="10" height="16" viewBox="0 0 10 16" fill="none" stroke="#111" stroke-width="2.6"><path d="m2 2 6 6-6 6"/></svg></div>

<div class="abs card" style="left:92px">
  <div class="photo" role="img" aria-label="Apprentice working in an office" style="inset:0;background:linear-gradient(160deg,#5b554c,#2c2b2a)"></div>
  <div class="icon"><svg width="36" height="36" viewBox="0 0 24 24" fill="none" stroke="#1e4a80" stroke-width="2" stroke-linecap="round"><path d="M12 3v3M12 18v3M3 12h3M18 12h3M5.6 5.6l2.1 2.1M16.3 16.3l2.1 2.1M5.6 18.4l2.1-2.1M16.3 7.7l2.1-2.1"/></svg></div>
  <h3>Apprentice Matching</h3><p>Lorem ipsum dolor sit amet, consectetur</p><div class="more">Read More</div><div class="bar"></div>
</div>
<div class="abs card" style="left:440px">
  <div class="photo" role="img" aria-label="Professionals networking in a meeting" style="inset:0;background:linear-gradient(160deg,#6e6a68,#333)"></div>
  <div class="icon"><svg width="34" height="34" viewBox="0 0 24 24" fill="none" stroke="#1e4a80" stroke-width="2"><circle cx="12" cy="12" r="9"/><path d="M8 10l-2 2 2 2M16 10l2 2-2 2"/></svg></div>
  <h3>Industry Networking</h3><p>Lorem ipsum dolor sit amet, consectetur</p><div class="more">Read More</div><div class="bar"></div>
</div>
<div class="abs card" style="left:787px">
  <div class="photo" role="img" aria-label="Apprentice in safety vest and helmet in a warehouse" style="inset:0;background:linear-gradient(160deg,#4a4d3a,#2d2f2a 60%,#6b7040)"></div>
  <div class="icon"><svg width="36" height="36" viewBox="0 0 24 24" fill="none" stroke="#1e4a80" stroke-width="2"><circle cx="7.5" cy="14" r="3"/><circle cx="16.5" cy="14" r="3"/><path d="M4 8h16M6 5h12"/></svg></div>
  <h3>Career Guidance</h3><p>Lorem ipsum dolor sit amet, consectetur</p><div class="more">Read More</div><div class="bar"></div>
</div>
<div class="abs btn" style="left:511px;top:2070px;width:168px;height:46px">Contact Us</div>

<!-- cta -->
<div class="abs cta" role="img" aria-label="Team of colleagues in a dark blue tinted office scene"></div>
<div class="abs cta-title">Delivering Results with Solid Dependability</div>
<div class="abs cta-quote">Get A Quote</div>
<div class="abs cta-phone"><svg width="18" height="18" viewBox="0 0 24 24" fill="#111"><path d="M6.6 10.8a15 15 0 0 0 6.6 6.6l2.2-2.2a1 1 0 0 1 1-.25 11.4 11.4 0 0 0 3.6.57 1 1 0 0 1 1 1V20a1 1 0 0 1-1 1A17 17 0 0 1 3 4a1 1 0 0 1 1-1h3.5a1 1 0 0 1 1 1c0 1.25.2 2.45.57 3.57a1 1 0 0 1-.25 1z"/></svg>0800 - 555 - 0147</div>

<!-- why choose us -->
<div class="abs label" style="left:515px;top:2444px">
  <span class="line"></span>Why Chose Us<span class="line"></span></div>
<h2 class="abs title" style="left:0;top:2466px;width:1200px;text-align:center">Why Choose Us</h2>
<div class="photo" role="img" aria-label="Smiling business consultant with arms crossed" style="left:434px;top:2575px;width:328px;height:363px;border-radius:50% 50% 50% 50%/45% 45% 55% 55%;background:radial-gradient(circle at 50% 40%,#8d98a6,#2e3a5a 80%)"></div>

<div class="abs why-item" style="left:120px;top:2615px;width:202px;text-align:right"><h4>Tailored Solutions</h4><p>Lorem ipsum dolor sit amet,<br>consectetur adipiscing elit</p></div>
<div class="abs why-icon" style="left:355px;top:2618px"><svg width="34" height="34" viewBox="0 0 24 24" fill="none" stroke="#f25c05" stroke-width="2"><circle cx="12" cy="4" r="2"/><path d="M4 9h16M12 9v5M12 14l-4 7M12 14l4 7"/></svg></div>
<div class="abs why-item" style="left:60px;top:2740px;width:238px;text-align:right"><h4>Industry Connections</h4><p>Lorem ipsum dolor sit amet,<br>consectetur adipiscing elit</p></div>
<div class="abs why-icon" style="left:319px;top:2743px"><svg width="34" height="34" viewBox="0 0 24 24" fill="none" stroke="#f25c05" stroke-width="2" stroke-linecap="round"><path d="M12 3v3M12 18v3M3 12h3M18 12h3M5.6 5.6l2.1 2.1M16.3 16.3l2.1 2.1M5.6 18.4l2.1-2.1M16.3 7.7l2.1-2.1"/></svg></div>
<div class="abs why-item" style="left:110px;top:2865px;width:192px;text-align:right"><h4>Global Reach</h4><p>Lorem ipsum dolor sit amet,<br>consectetur adipiscing elit</p></div>
<div class="abs why-icon" style="left:352px;top:2866px"><svg width="34" height="34" viewBox="0 0 24 24" fill="none" stroke="#f25c05" stroke-width="2"><path d="M4 14a8 8 0 0 1 16 0v3H4z"/><path d="M4 11h16M9 17v3h6v-3"/></svg></div>

<div class="abs why-icon" style="left:763px;top:2618px"><svg width="34" height="34" viewBox="0 0 24 24" fill="none" stroke="#f25c05" stroke-width="2"><circle cx="12" cy="12" r="9"/><circle cx="12" cy="12" r="5"/><circle cx="12" cy="12" r="1.5"/></svg></div>
<div class="abs why-item" style="left:891px;top:2615px;width:230px"><h4>Connections</h4><p>Lorem ipsum dolor sit amet,<br>consectetur adipiscing elit</p></div>
<div class="abs why-icon" style="left:795px;top:2743px"><svg width="34" height="34" viewBox="0 0 24 24" fill="none" stroke="#f25c05" stroke-width="2"><path d="M4 14a8 8 0 0 1 16 0v3H4z"/><path d="M4 11h16M9 17v3h6v-3"/></svg></div>
<div class="abs why-item" style="left:899px;top:2740px;width:230px"><h4>Skill Development</h4><p>Lorem ipsum dolor sit amet,<br>consectetur adipiscing elit</p></div>
<div class="abs why-icon" style="left:763px;top:2866px"><svg width="34" height="34" viewBox="0 0 24 24" fill="none" stroke="#f25c05" stroke-width="2"><rect x="3" y="3" width="6" height="6"/><rect x="15" y="15" width="6" height="6"/><path d="M9 6h9v9M15 18H6V9"/></svg></div>
<div class="abs why-item" style="left:876px;top:2865px;width:230px"><h4>Support System</h4><p>Lorem ipsum dolor sit amet,<br>consectetur adipiscing elit</p></div>

<!-- testimonials -->
<section class="abs testi-bg"></section>
<div class="photo" role="img" aria-label="Group of colleagues in a blue tinted office" style="left:0;top:3058px;width:338px;height:534px;background:linear-gradient(160deg,#2b3a5c,#46557a 50%,#1f2b48)"></div>
<div class="abs label" style="left:574px;top:3120px"><span class="line"></span>Testimonials<span class="line"></span></div>
<h2 class="abs title" style="left:338px;top:3142px;width:666px;text-align:center">What Clients are Saying</h2>

<div class="abs tcard" style="left:135px;width:347px">
  <p>Lorem ipsum dolor sit amet, consectetur adipis por incididunt ut labore et dolore magna aliqu uis nostrud exercitation ullamco laboris nisi consequat. Duis aute irure dolor in reprehend</p>
  <div class="who"><span class="avatar"></span>Lena Marti</div><div class="qmark">”</div>
</div>
<div class="abs tcard" style="left:500px;width:343px;border-bottom:3px solid var(--blue)">
  <p>Lorem ipsum dolor sit amet, consectetur adipis por incididunt ut labore et dolore magna aliqu uis nostrud exercitation ullamco laboris nisi consequat. Duis aute irure dolor in reprehend</p>
  <div class="who"><span class="avatar"></span>Lena Marti</div><div class="qmark">”</div>
</div>
<div class="abs tcard" style="left:870px;width:340px">
  <p>Lorem ipsum dolor sit amet, consectetur adipis por incididunt ut labore et dolore magna aliqu uis nostrud exercitation ullamco laboris nisi consequat. Duis aute irure dolor in reprehend</p>
  <div class="who"><span class="avatar"></span>Lena Marti</div><div class="qmark" style="right:36px">”</div>
</div>
<div class="abs" style="left:631px;top:3501px;width:24px;height:24px;border-radius:50%;border:1.5px solid var(--blue)"></div>
<div class="abs dot" style="left:638px;background:var(--blue)"></div>
<div class="abs dot" style="left:662px"></div>
<div class="abs dot" style="left:692px"></div>
<div class="abs dot" style="left:722px"></div>

<!-- contact -->
<div class="abs label" style="left:530px;top:3716px"><span class="line"></span>Contact Us<span class="line"></span></div>
<h2 class="abs title" style="left:0;top:3738px;width:1260px;text-align:center">Get in touch with us</h2>
<div class="photo" role="img" aria-label="Two colleagues reviewing a tablet together" style="left:91px;top:3845px;width:420px;height:415px;background:linear-gradient(135deg,#dfe3e7,#8c98a6 55%,#3a4150)"></div>
<div class="abs" style="left:284px;top:4184px;width:198px;height:52px;background:#fff;display:flex;align-items:center;justify-content:center;gap:12px;font-size:16px;color:var(--ink)"><svg width="18" height="18" viewBox="0 0 24 24" fill="#111"><path d="M6.6 10.8a15 15 0 0 0 6.6 6.6l2.2-2.2a1 1 0 0 1 1-.25 11.4 11.4 0 0 0 3.6.57 1 1 0 0 1 1 1V20a1 1 0 0 1-1 1A17 17 0 0 1 3 4a1 1 0 0 1 1-1h3.5a1 1 0 0 1 1 1c0 1.25.2 2.45.57 3.57a1 1 0 0 1-.25 1z"/></svg>0800-555-014</div>
<div class="abs form-panel"></div>
<h3 class="abs" style="left:554px;top:3891px;font-size:23px;font-weight:600;color:var(--ink)">Get a free consultation</h3>
<p class="abs" style="left:554px;top:3934px;width:500px;font-size:13px;line-height:23px;color:var(--muted)">Get a free consultation from our experts, Our customer support team help you 24/7. Don't hesitate.</p>
<div class="abs field" style="left:554px;top:4011px;width:501px;height:48px">Your Name</div>
<div class="abs field" style="left:554px;top:4081px;width:237px;height:49px">Your Email</div>
<div class="abs field" style="left:816px;top:4081px;width:237px;height:49px">Message</div>
<div class="abs btn" style="left:554px;top:4149px;width:501px;height:49px;font-size:11px;gap:8px">GET IN TOUCH <svg width="14" height="10" viewBox="0 0 14 10" fill="none" stroke="#fff" stroke-width="1.6"><path d="M1 5h11M8 1l4 4-4 4"/></svg></div>

<!-- footer -->
<div class="abs" style="left:115px;top:4373px;width:975px;height:40px;background:#d7e2ee;clip-path:polygon(2% 0,100% 70%,100% 100%,0 100%)"></div>
<footer class="abs footer"></footer>
<div class="abs infobox">
  <div><svg width="44" height="40" viewBox="0 0 24 24" fill="none" stroke="#f25c05" stroke-width="1.3"><path d="M12 14s5-5 5-8.5a5 5 0 0 0-10 0C7 9 12 14 12 14z"/><circle cx="12" cy="5.5" r="1.8"/><path d="M3 22l3-8h3M21 22l-3-8h-3M3 22h18"/></svg>Come to Our Location</div>
  <div><svg width="44" height="40" viewBox="0 0 24 24" fill="none" stroke="#f25c05" stroke-width="1.3"><path d="M3 9l9 6 9-6v12H3z"/><path d="M3 9l9-6 9 6"/><path d="M6 7V5h12v2"/></svg>Send Us an Email</div>
  <div><svg width="44" height="40" viewBox="0 0 24 24" fill="none" stroke="#f25c05" stroke-width="1.3"><rect x="8" y="2" width="8" height="20" rx="1.5"/><path d="M11 19h2M19 9a4 4 0 0 1 0 6M21 7a7 7 0 0 1 0 10"/></svg>Give Us a Call</div>
</div>
<div class="abs logo" style="left:102px;top:4600px;font-size:50px">lernwandel</div>
<p class="abs ft-t" style="left:85px;top:4690px;width:320px">Lorem ipsum dolor sit amet, consectetur adipi por incididunt ut labore et dolore magna aliqu uis nostrud exercitation ullamco laboris nisi ut a consequat. Duis aute irure dolor in reprehend</p>
<div class="abs ft-h" style="left:438px;top:4614px">Visit Our Place</div>
<p class="abs ft-t" style="left:438px;top:4690px">12 Lernweg<br>3011 Bern, Switzerland</p>
<div class="abs" style="left:438px;top:4746px;font-size:11px;font-weight:700;color:#fff">FIND US ON MAP</div>
<div class="abs" style="left:438px;top:4796px;width:307px;height:40px;border-bottom:1px solid #c6ced9;border-right:1px solid #c6ced9"></div>
<div class="abs" style="left:450px;top:4810px;font-size:11px;color:#c6ced9">Enter Your Email...</div>
<div class="abs" style="left:644px;top:4796px;width:1px;height:40px;background:#c6ced9"></div>
<div class="abs" style="left:656px;top:4809px;font-size:12px;font-weight:700;color:var(--orange)">SUBSCRIBE</div>
<div class="abs ft-h" style="left:791px;top:4614px">Useful Links</div>
<div class="abs ft-link" style="left:789px;top:4688px">About Us</div>
<div class="abs ft-link" style="left:789px;top:4721px">Practice areas</div>
<div class="abs ft-link" style="left:789px;top:4754px">Why Choose Us</div>
<div class="abs ft-link" style="left:789px;top:4787px">How it works</div>
<div class="abs ft-link" style="left:789px;top:4822px">News &amp; Updates</div>
<div class="abs ft-link" style="left:959px;top:4688px">Testimonials</div>
<div class="abs ft-link" style="left:959px;top:4721px">FAQs</div>
<div class="abs ft-link" style="left:959px;top:4754px">Cookies</div>
<div class="abs ft-link" style="left:959px;top:4787px">Contact Us</div>
<div class="abs ft-link" style="left:959px;top:4822px">Privacy Policy</div>

<div class="abs bottom"></div>
<div class="abs" style="left:85px;top:4930px;font-size:11px;font-weight:600;color:var(--ink)">Lernwandel Apprenticeship Exchange</div>
<div class="abs" style="left:993px;top:4933px;width:9px;height:9px;border-radius:50%;background:#1a1a1a"></div>
<div class="abs" style="left:1031px;top:4933px;width:9px;height:9px;border-radius:50%;background:#1a1a1a"></div>
<div class="abs" style="left:1070px;top:4933px;width:9px;height:9px;border-radius:50%;background:#1a1a1a"></div>
<div class="abs" style="left:1108px;top:4933px;width:9px;height:9px;background:#1a1a1a"></div>
<div class="abs" style="left:1138px;top:4900px;width:49px;height:48px;background:var(--orange);border-radius:3px;display:flex;align-items:center;justify-content:center"><svg width="18" height="12" viewBox="0 0 18 12" fill="none" stroke="#fff" stroke-width="2.4"><path d="M2 10l7-7 7 7"/></svg></div>

</body>
</html>
```